Lumo4Kart - a fintech company - business card

We need a business card design for our Payments Technology company in Sydney, Australia. We provide business with payment solutions expanding across EFTPOS machines, online payment gateways and mobile payment solutions. We would like to see designs that are clean, classy and professional.
Target Market(s)
Business professionals, executives, c-suite
Industry/Entity Type
Fintech
Contact Information for Business Card
Will be on 400gsm. Logo will most likely be spot gloss unless designer recommends otherwise.
Font styles to use
Sans Serif
Requirements
Must have
- We need our website (lumo4kart.com.au), email (contact@lumo4kart.com.au), mobile (0432 587 904) and direct phone number (02 6815 3927) to feature on the card along with our logo (attached) and the words "EFTPOS | ONLINE | MOBILE"
- Font = Roboto

```html
<!DOCTYPE html>
<html lang="en">
<head>
<meta charset="utf-8">
<title>Lumo4Kart business card</title>
<link rel="stylesheet" href="https://fonts.googleapis.com/css2?family=Roboto:wght@400;500;700&display=swap">
<style>
  :root {
    --brand-blue: #1a5b8e;
    --ink-grey: #5f6165;
    --band-grey: #6a6c70;
    --soft-grey: #e3e4e6;
    --card-white: #f6f6f6;
    --page: #dcdcdc;
  }
  * { box-sizing: border-box; margin: 0; padding: 0; }
  html, body { width: 1200px; height: 1200px; overflow: hidden; }
  body {
    background: var(--page);
    font-family: "Roboto", Arial, sans-serif;
    position: relative;
  }
  .card {
    position: absolute;
    left: 170px;
    width: 860px;
    height: 491px;
    background: var(--card-white);
    overflow: hidden;
    box-shadow: 0 6px 18px rgba(0,0,0,.18);
  }
  .card--back { top: 75px; }
  .card--front { top: 634px; }
  .card__art { position: absolute; inset: 0; width: 100%; height: 100%; }

  .wordmark {
    position: absolute;
    display: flex;
    align-items: center;
    gap: 14px;
  }
  .wordmark__dot {
    border-radius: 50%;
    background: var(--brand-blue);
    flex: none;
  }
  .wordmark__name {
    color: var(--ink-grey);
    font-weight: 700;
    text-transform: uppercase;
    letter-spacing: .5px;
    line-height: 1;
    white-space: nowrap;
  }

  /* contact side */
  .card--back .wordmark { left: 360px; top: 150px; }
  .card--back .wordmark__dot { width: 40px; height: 40px; }
  .card--back .wordmark__name { font-size: 40px; }
  .services {
    position: absolute;
    left: 362px; top: 204px;
    color: var(--brand-blue);
    font-size: 13.5px;
    font-weight: 500;
    letter-spacing: .6px;
  }
  .contact-row {
    position: absolute;
    left: 362px;
    display: flex;
    align-items: center;
    gap: 16px;
    color: var(--ink-grey);
    font-size: 18px;
    font-weight: 500;
    line-height: 1.3;
    letter-spacing: .4px;
    white-space: nowrap;
  }
  .contact-row--phone { top: 246px; }
  .contact-row--web { top: 322px; }
  .contact-row__icon {
    width: 38px; height: 38px;
    background: var(--brand-blue);
    display: flex; align-items: center; justify-content: center;
    flex: none;
  }

  /* brand side */
  .card--front .wordmark { left: 250px; top: 218px; }
  .card--front .wordmark__dot { width: 62px; height: 62px; }
  .card--front .wordmark__name { font-size: 66px; }
</style>
</head>
<body>

<section class="card card--back" aria-label="Business card, contact side">
  <svg class="card__art" viewBox="0 0 860 491" aria-hidden="true">
    <circle cx="560" cy="110" r="175" fill="var(--soft-grey)"/>
    <circle cx="560" cy="520" r="120" fill="var(--soft-grey)"/>
    <circle cx="-10" cy="300" r="330" fill="var(--brand-blue)"/>
    <circle cx="880" cy="240" r="125" fill="var(--brand-blue)"/>
  </svg>

  <div class="wordmark">
    <span class="wordmark__dot"></span>
    <span class="wordmark__name">Lumo4Kart</span>
  </div>
  <p class="services">EFTPOS | ONLINE | MOBILE</p>

  <div class="contact-row contact-row--phone">
    <span class="contact-row__icon">
      <svg width="20" height="20" viewBox="0 0 24 24" aria-hidden="true">
        <path fill="#fff" d="M6.6 10.8a15.1 15.1 0 0 0 6.6 6.6l2.2-2.2a1 1 0 0 1 1-.25 11.4 11.4 0 0 0 3.6.57 1 1 0 0 1 1 1V20a1 1 0 0 1-1 1A17 17 0 0 1 3 4a1 1 0 0 1 1-1h3.5a1 1 0 0 1 1 1c0 1.25.2 2.45.57 3.57a1 1 0 0 1-.25 1z"/>
      </svg>
    </span>
    <div>0432 587 904<br>02 6815 3927</div>
  </div>

  <div class="contact-row contact-row--web">
    <span class="contact-row__icon">
      <svg width="20" height="20" viewBox="0 0 24 24" aria-hidden="true" fill="none" stroke="#fff" stroke-width="1.6">
        <circle cx="12" cy="12" r="9"/>
        <ellipse cx="12" cy="12" rx="4" ry="9"/>
        <path d="M3 12h18M5 7h14M5 17h14"/>
      </svg>
    </span>
    <div>contact@lumo4kart.com.au<br>lumo4kart.com.au</div>
  </div>
</section>

<section class="card card--front" aria-label="Business card, brand side">
  <svg class="card__art" viewBox="0 0 860 491" aria-hidden="true">
    <circle cx="720" cy="200" r="200" fill="var(--soft-grey)"/>
    <circle cx="150" cy="280" r="140" fill="var(--soft-grey)"/>
    <circle cx="170" cy="-30" r="200" fill="var(--brand-blue)"/>
    <circle cx="400" cy="-60" r="120" fill="var(--brand-blue)"/>
    <polygon points="0,385 680,420 645,475 0,440" fill="var(--brand-blue)"/>
    <polygon points="690,420 860,428 860,491 660,480" fill="var(--band-grey)"/>
  </svg>

  <div class="wordmark">
    <span class="wordmark__dot"></span>
    <span class="wordmark__name">Lumo4Kart</span>
  </div>
</section>

</body>
</html>
```